Celebrity News Site

We need a new 1 Page (homepage) layout for a new website we are developing. It will be coded "responsive" to work on both larger and smaller screens.

We like the colors (bright and lots of white) from these sites: http://www.brightlanepost.example www.velmarigazette.example

We like a narrow navigation across the top, preferibly with a black background.

The site will mostly be made up of photos and ads.

I've done a sample layout. And attached our logo.
Updates

Sorry if there was any confusion. I just need one page (homepage) design. Not a full site. Added Tuesday, February 7, 2017

Target Market(s)

USA

Industry/Entity Type

News

Number of Pages Required

1 page

Colors
e34197
eea4c8
ffffff
f59195
f04a50
ec1f27

Requirements
Must have
• Thin, black nav bar at the top.
Nice to have
• Bright colors, white background
Should not have
• some of the bright colors I listed below.

```html
<!DOCTYPE html>
<html lang="en">
<head>
<meta charset="utf-8">
<title>Glintpost – Celebrity News</title>
<link href="https://fonts.googleapis.com/css2?family=Lato:wght@400;700&family=Roboto:wght@400&display=swap" rel="stylesheet">
<style>
:root{
  --ink:#111;
  --bar:#1b1b1b;
  --pink:#e34197;
  --sky:#4fc1ea;
  --link:#3fa9e0;
  --grey:#555;
  --line:#d6d6d6;
  --caption:rgba(30,30,30,.85);
  --white:#fff;
}
*{box-sizing:border-box;margin:0;padding:0}
html,body{width:968px;height:1200px;overflow:hidden;background:var(--white);font-family:"Lato",sans-serif;color:var(--ink)}
.page{position:relative;width:968px;height:1200px}
.abs{position:absolute}

/* top nav */
.topbar{left:0;top:0;width:968px;height:58px;background:var(--bar)}
.brand{left:46px;top:10px;font-size:34px;font-weight:700;color:var(--pink);letter-spacing:-.5px;line-height:38px}
.search{left:311px;top:14px;width:346px;height:29px;background:#3a3a3a;border:1px solid #555;border-radius:3px;color:#9a9a9a;font-size:12px;line-height:27px;padding-left:11px;font-family:"Roboto",sans-serif}
.search svg{position:absolute;right:14px;top:6px}
.nav{left:721px;top:18px;display:flex;gap:21px;color:var(--white);font-size:15.5px;letter-spacing:.3px}

/* hero */
.hero{left:46px;top:74px;width:567px;height:125px;background:linear-gradient(180deg,#6f8fb5 0%,#9fb4c9 40%,#7c8a92 60%,#8e6e55 100%)}
.hero-title{left:67px;top:126px;color:var(--white);font-size:21px}
.btn-dark{left:490px;top:124px;width:103px;height:30px;background:#0d0d0d;border-radius:5px;color:var(--white);font-size:11.5px;text-align:center;line-height:30px;letter-spacing:.3px}

/* tiles */
.tile{width:180px;overflow:hidden}
.tile .photo{width:100%;height:100%}
.tile .cap{position:absolute;left:0;bottom:0;width:100%;height:48px;background:var(--caption);color:var(--white);font-size:17px;padding-left:24px;line-height:48px}
.row1{top:221px;height:226px}
.row2{top:469px;height:238px}

/* shoe banner */
.promo{left:46px;top:736px;width:567px;height:157px;background:linear-gradient(90deg,#c9ab86 0%,#b48866 40%,#c65a33 65%,#a89178 100%)}
.promo-title{left:56px;top:799px;width:375px;height:45px;background:rgba(255,255,255,.75);font-size:22.5px;padding-left:12px;line-height:45px}
.btn-outline{left:487px;top:805px;width:115px;height:36px;border:2px solid #111;border-radius:6px;text-align:center;line-height:32px;font-size:13.5px}

/* sidebar */
.feature{left:625px;top:74px;width:297px;height:261px;background:linear-gradient(120deg,#b7b3ad 0%,#d9d2cb 50%,#e9e5e0 100%)}
.feature-text{left:760px;top:102px;width:141px;text-align:right;font-size:17.5px;line-height:22.3px}
.news-bar{left:625px;top:351px;width:297px;height:24px;background:#4a4a4a;color:var(--white);font-size:18px;padding-left:11px;line-height:26px;letter-spacing:.3px}
.news-sub{left:623px;top:383px;font-size:16px;color:#8a8a8a}
.email{left:623px;top:416px;width:299px;height:43px;border:1px solid #ccc;color:#aaa;font-size:14px;padding:7px 10px}
.subscribe{left:623px;top:473px;width:299px;height:37px;background:var(--sky);color:var(--white);font-size:22px;text-align:center;line-height:37px;letter-spacing:2.5px}
.tweets-h{left:628px;top:528px;font-family:"Roboto",sans-serif;font-size:24px;color:#333}
.tweets-h small{font-size:14px;color:#999}
.tweets-h span{font-size:17px;color:var(--link)}
.tweet-box{left:625px;top:568px;width:297px;height:326px;border-top:1px solid var(--line);overflow:hidden;font-family:"Roboto",sans-serif}
.tags{left:627px;top:585px;font-size:14px;color:#444}
.tweet-photo{left:627px;top:618px;width:264px;height:136px;border-radius:5px;background:linear-gradient(180deg,#4b4458 0%,#3d3a4f 50%,#2c2f3e 100%)}
.tweet-meta{left:627px;top:768px;width:264px;height:20px;color:#ccc;font-size:13px}
.tweet-sep{left:625px;top:804px;width:277px;height:1px;background:var(--line)}
.avatar{left:627px;top:818px;width:37px;height:37px;border-radius:4px;background:#1d4a4f}
.handle{left:674px;top:825px;color:var(--link);font-size:17px}
.tweet-line{left:627px;top:868px;font-size:14px;color:#333}
.scroll{left:902px;top:568px;width:20px;height:326px;border-left:1px solid #eee}
.scroll .thumb{position:absolute;left:3px;top:118px;width:14px;height:18px;background:#c8c8c8}

/* footer */
.footer{left:0;top:921px;width:968px;height:234px;background:var(--bar);color:var(--white)}
.copy{left:0;top:1155px;width:968px;height:45px;background:#111;color:#ddd;font-size:12px;text-align:center;line-height:44px}
.fh{top:948px;font-size:16.5px;color:var(--white);letter-spacing:.2px}
.about{left:47px;top:984px;width:240px;font-size:12.5px;line-height:22.7px;color:#eee}
.cats{left:354px;top:986px;list-style:none;font-size:11.8px;line-height:22.3px;color:#eee}
.cats li:first-child{color:var(--pink)}
.posts{left:530px;top:985px;font-size:12.5px;line-height:22.5px;color:#eee}
.posts b{font-weight:700;color:var(--white)}
.social{left:777px;top:988px;display:flex;gap:14px}
.social span{width:15px;height:15px;border-radius:50%;background:var(--white)}
.social span:first-child{background:var(--pink)}
</style>
</head>
<body>
<div class="page">

  <header class="abs topbar"></header>
  <div class="abs brand">Glintpost</div>
  <div class="abs search">Search for your favorite Athletes or celebrities !
    <svg width="17" height="17" viewBox="0 0 17 17"><circle cx="7" cy="7" r="5.5" fill="none" stroke="#ddd" stroke-width="2"/><line x1="11" y1="11" x2="16" y2="16" stroke="#ddd" stroke-width="2"/></svg>
  </div>
  <nav class="abs nav"><span>CELEBS</span><span>BEAUTY</span><span>STYLE</span></nav>

  <div class="abs hero" role="img" aria-label="City skyline by the sea with a tiled tower"></div>
  <div class="abs hero-title">Lorem ipsum dolor sit amet consectetur</div>
  <div class="abs btn-dark">CONTACT US</div>

  <div class="abs tile row1" style="left:46px"><div class="photo" role="img" aria-label="Woman in a gold dress by a pink sofa" style="background:linear-gradient(160deg,#b5aea5,#c45a6a 70%,#6a5a4a)"></div><div class="cap">Lorem ipsum dolo</div></div>
  <div class="abs tile row1" style="left:240px"><div class="photo" role="img" aria-label="Man in a white jacket" style="background:linear-gradient(160deg,#2e4a63,#b6bcc4 60%,#e4e4e4)"></div><div class="cap">Lorem ipsum dolo</div></div>
  <div class="abs tile row1" style="left:433px"><div class="photo" role="img" aria-label="Smiling woman in a striped top" style="background:linear-gradient(160deg,#6fc6c3,#8ccfcc 50%,#5a5a5a)"></div><div class="cap">Lorem ipsum dolo</div></div>

  <div class="abs tile row2" style="left:46px"><div class="photo" role="img" aria-label="Red-haired woman portrait" style="background:linear-gradient(160deg,#e8ccc8,#c8866a 60%,#e7a2a6)"></div><div class="cap">Lorem ipsum dolo</div></div>
  <div class="abs tile row2" style="left:240px"><div class="photo" role="img" aria-label="Mother lifting a baby outdoors" style="background:linear-gradient(160deg,#5fb6cc,#d9e4e6 55%,#d8b49a)"></div><div class="cap">Lorem ipsum dolo</div></div>
  <div class="abs tile row2" style="left:433px"><div class="photo" role="img" aria-label="Man in a dark suit by an iron gate" style="background:linear-gradient(160deg,#3b4358,#6b7387 50%,#1f2535)"></div><div class="cap">Lorem ipsum dolo</div></div>

  <div class="abs promo" role="img" aria-label="Orange leather boots on a wooden table"></div>
  <div class="abs promo-title">Adipiscing elit Etiam blandit nulla et</div>
  <div class="abs btn-outline">SEE MORE</div>

  <aside>
    <div class="abs feature" role="img" aria-label="Woman in a pink dress lying on sand"></div>
    <div class="abs feature-text">Lorem ipsum dolor sit amet consectetur ad ipiscing elit. Etiam blandit nulla et egestas vestibulum magna tortor</div>

    <div class="abs news-bar">NEWSLETTER</div>
    <div class="abs news-sub">Subscribe to our newsletter</div>
    <div class="abs email">Your Email Address</div>
    <div class="abs subscribe">SUBSCRIBE</div>

    <div class="abs tweets-h">Tweets <small>by</small> <span>@lorem ipsum</span></div>
    <div class="abs tweet-box"></div>
    <div class="abs tags">#Pressleaf #Translation #Office</div>
    <div class="abs tweet-photo" role="img" aria-label="River at dusk with a passing boat"></div>
    <div class="abs tweet-meta">
      <svg width="16" height="14" viewBox="0 0 16 14" style="position:absolute;left:2px;top:0"><path d="M8 13 1.5 6.5A3.6 3.6 0 0 1 8 2.5a3.6 3.6 0 0 1 6.5 4Z" fill="#ddd"/></svg>
      <svg width="16" height="14" viewBox="0 0 16 14" style="position:absolute;left:48px;top:0"><path d="M7 2H2v10h5M6 7h9M12 4l3 3-3 3" fill="none" stroke="#ccc" stroke-width="1.6"/></svg>
      <span style="position:absolute;right:0;top:0">05 Sep</span>
    </div>
    <div class="abs tweet-sep"></div>
    <div class="abs avatar"></div>
    <div class="abs handle">loremipsum@mailbox.example</div>
    <div class="abs tweet-line">Verandel 1.0.1 - Pressleaf Theme /</div>
    <div class="abs scroll">
      <svg width="20" height="326" viewBox="0 0 20 326" style="position:absolute;left:0;top:0"><path d="M6 16 10 11 14 16Z" fill="#333"/><path d="M6 310 10 315 14 310Z" fill="#333"/></svg>
      <div class="thumb"></div>
    </div>
  </aside>

  <footer class="abs footer"></footer>
  <div class="abs fh" style="left:46px">ABOUT US</div>
  <div class="abs fh" style="left:355px">CATEGORIES</div>
  <div class="abs fh" style="left:530px">LATEST POSTS</div>
  <div class="abs fh" style="left:777px">FOLLOW US</div>
  <p class="abs about">Lorem ipsum dolor sit amet, consectetur adipisicing elit, sed do eiusmod tempor incididunt ut labore. Lorem ipsum dolor sit amet, consectetur adipisicing elit, sed do eiusmod tempor incid idunt ut labore Lorem ipsum dolo.</p>
  <ul class="abs cats"><li>Entertaiment</li><li>Feature</li><li>video</li><li>Politic</li><li>Sport</li><li>Writting</li></ul>
  <div class="abs posts">
    <b>Who made dummy text?</b><br>July 19, 2012 &nbsp;// &nbsp;8 Comments<br>
    <b>Gallery</b><br>November 18, 2012 &nbsp;// &nbsp;No Comment<br>
    <b>The Greate Wall</b><br>July 19, 2012 &nbsp;// &nbsp;1 Comment
  </div>
  <div class="abs social" aria-label="Social links"><span></span><span></span><span></span><span></span><span></span><span></span></div>
  <div class="abs copy">Copyright © . All Rights Reserved</div>

</div>
</body>
</html>
```